New Digital Marketing Company Needs Web Design

Introduction

Pixelbrook gives advice to small businesses about their websites and digital marketing strategies and builds working relationships with clients to understand their business and maximise its online presence.

Pixelbrook offers services to support its clients needs such as: website auditing & search engine optimisation (SEO), Zorvani Promoline, Chatterloop advertising, newsletter development & management, online performance reporting, email setup & management, website hosting, maintenance & backup, web development, web updates & web design.

Design Specification

The site should have a clean & professional look and use the colour scheme from the logo (attached below).

The design should consist of 2 templates; The homepage & content page.

Homepage Design

The homepage should have a header with logo, contact number and email and menu. Followed underneath by a slider and then individual blocks for key services. Under the key services should be a testimonial block with 3 testimonials. Finally the footer with company details, menu links and location map.

Header Info:

Contact number: 01632 960418
Email: info@pixelbrook.co.uk

Menu: Home Services About Contact

Slider Design:

The slider should be full page and show an image with text.

Key Services:

The key services should have a relevant icon and brief description.

The key services are:

Digital Marketing

Website Hosting & Management

Website Health Check (SEO)

Website Updating & Development

Newsletter Management

Email Management

Note: Lorem Ipsum can be used for brief description...

Testimonials:

There should be 3 testimonials side by side and they should include a headshot image of the person giving the testimonial.

Note: Lorem Ipsum and sample images can be used for testimonials...

Footer:

The footer should have 3 sections:

Menu links:

Digital Marketing About
Zorvani Promoline Contact
Chatterloop Advertising Privacy Policy
Search Engine Optimisation (SEO) Terms & Conditions
Website Hosting FAQ
Newsletter Management

Company Information:

PixelBrook
14 Farrow Close
Dunmere
Westshire
ZX47 3LT
Tel: 01632 960418

Chatterloop icon - Quillo icon - Guildnet icon

Location

Zorvani map

Footer Bottom:

Copyright message.

Content Design

The content design should have the common header and footer.

Each content page should have a banner for image with text description (page title).

The content page should have area for text description and area for a video display if available.

There should be a right column (possibly) for modules (latest blog, latest Chatterloop feeds, testimonial)
Updates

Reason: I have had to extend the deadline as could not review while on vacation and need to feedback to some designers for content page design. Many thanks for your understanding.

Target Market(s)

Industry/Entity Type

Digital

Number of Pages Required

2 page

Requirements
Must have
• The site should have a clean & professional look and use the colour scheme from the logo (attached below).
• The design should consist of 2 templates; The homepage & content page.

```html
<!DOCTYPE html>
<html lang="en">
<head>
<meta charset="utf-8">
<title>PixelBrook – Digital Marketing</title>
<link rel="stylesheet" href="https://fonts.googleapis.com/css2?family=Lato:ital,wght@0,400;0,700;1,400&family=Tinos&family=Roboto+Slab:wght@700&display=swap">
<style>
:root{
  --plum:#6b1d4d;
  --plum-dark:#5a1741;
  --ink:#3b2d52;
  --circle:#4b3d60;
  --circle-seo:#7b2a5a;
  --text:#444;
  --grey-bg:#efefef;
  --light-bg:#f4f4f4;
  --footer:#0d0d0d;
  --white:#fff;
}
*{box-sizing:border-box;margin:0;padding:0}
html,body{width:1200px;height:2332px;overflow:hidden;background:var(--white)}
body{font-family:"Lato",sans-serif;color:var(--text);position:relative}
.abs{position:absolute}

/* header */
.site-header{position:absolute;left:0;top:0;width:1200px;height:94px;background:var(--white)}
.topbar{position:absolute;left:427px;top:0;right:0;height:30px;background:var(--plum);clip-path:polygon(0 0,100% 0,100% 100%,48px 100%)}
.topbar .contact{position:absolute;top:5px;color:var(--white);font-size:14px;display:flex;align-items:center;gap:8px;white-space:nowrap}
.topbar .mail{left:286px}
.topbar .phone{left:506px;font-size:19px;font-weight:700;top:3px}
.brand{position:absolute;left:128px;top:22px;display:flex;align-items:center;gap:12px}
.brand-dot{width:34px;height:34px;border-radius:50%;background:var(--plum)}
.brand-name{font-size:38px;font-weight:700;color:var(--plum);letter-spacing:-0.5px}
.main-nav{position:absolute;left:0;top:0;width:1200px;height:94px;font-size:15px;color:var(--ink)}
.nav-link{position:absolute;top:54px;color:inherit;text-decoration:none;white-space:nowrap}
.nav-home{left:555px}
.nav-about{left:660px}
.nav-services{left:797px}
.nav-contact{left:973px}
.nav-home::after{content:"";position:absolute;left:0;right:0;bottom:-6px;height:2px;background:var(--plum)}

/* hero */
.hero{position:absolute;left:0;top:94px;width:1200px;height:439px;
  background:radial-gradient(circle at 240px 240px,#d9a64a 0,#6a4a1c 60px,transparent 170px),
  radial-gradient(ellipse at 340px 150px,rgba(120,170,220,.55),transparent 260px),
  linear-gradient(90deg,#121721 0,#1d2536 45%,#05070b 100%)}
.hero-copy{position:absolute;right:129px;top:134px;text-align:right;font-family:"Tinos",serif;color:var(--white);font-size:20.5px;line-height:34px;white-space:nowrap}
.btn-start{position:absolute;right:136px;top:245px;width:150px;height:48px;background:var(--plum-dark);border:2px solid #8d6a8a;color:var(--white);font-size:21px;font-weight:700;display:flex;align-items:center;justify-content:center}
.slide-arrow{position:absolute;top:187px;width:34px;height:30px;background:#3a3a3a;border:1px solid #777;display:flex;align-items:center;justify-content:center}
.slide-arrow.prev{left:0}.slide-arrow.next{right:0}

/* section headings */
.sec-title{position:absolute;left:0;width:1200px;text-align:center;font-size:33px}
.divider{position:absolute;left:393px;width:414px;height:20px}
.divider::before{content:"";position:absolute;left:0;right:0;top:8px;height:1px;background:#aaa}
.divider::after{content:"";position:absolute;left:199px;top:1px;width:16px;height:16px;border-radius:50%;background:var(--plum);box-shadow:0 0 0 4px var(--white)}
.welcome .divider::after{box-shadow:0 0 0 4px var(--grey-bg)}
.testimonials .divider::after{box-shadow:0 0 0 4px var(--light-bg)}

/* welcome */
.welcome{position:absolute;left:0;top:533px;width:1200px;height:291px;background:var(--grey-bg)}
.welcome .sec-title{top:44px;color:var(--plum);font-weight:700}
.welcome .divider{top:87px}
.welcome-text{position:absolute;left:130px;width:940px;top:124px;text-align:center;font-size:12px;line-height:21.5px;color:#555}
.btn-more{position:absolute;left:544px;top:210px;width:112px;height:32px;border-radius:16px;background:var(--plum-dark);color:var(--white);font-size:12px;font-weight:700;display:flex;align-items:center;justify-content:center}

/* services */
.services{position:absolute;left:0;top:824px;width:1200px;height:772px;background:var(--white)}
.services .sec-title{top:40px;color:var(--plum);font-weight:700}
.services .divider{top:84px}
.service{position:absolute;width:300px}
.service h3{font-size:15.5px;font-weight:700;color:var(--ink);margin-bottom:4px}
.service.seo h3{color:var(--plum)}
.service p{font-size:12.5px;line-height:15px;color:#555}
.service.right{text-align:right}

/* testimonials */
.testimonials{position:absolute;left:0;top:1596px;width:1200px;height:429px;background:var(--light-bg)}
.testimonials .sec-title{top:38px;color:var(--plum)}
.testimonials .divider{top:82px}
.quote{position:absolute;top:154px;width:300px;text-align:center}
.headshot{width:110px;height:103px;margin:0 auto;border:3px solid var(--plum);border-radius:6px;background:linear-gradient(160deg,#cfd8e3,#8094ae)}
.quote p{margin-top:30px;font-size:12.5px;font-style:italic;line-height:15.5px;color:#444}
.quote .mark{position:absolute;left:-2px;top:132px;font-family:"Tinos",serif;font-size:110px;color:#ddd;line-height:1}
.quote cite{display:block;margin-top:12px;font-family:"Roboto Slab",serif;font-style:normal;font-weight:700;font-size:14px;color:var(--plum)}
.t-arrow{position:absolute;top:220px}

/* footer */
.site-footer{position:absolute;left:0;top:2025px;width:1200px;height:266px;background:var(--footer);color:#ddd}
.f-col{position:absolute;top:36px}
.f-col h4{font-size:17px;font-weight:400;color:var(--white);padding-bottom:9px;border-bottom:1px solid #333;width:186px}
.f-col h4 span{color:var(--plum)}
.links{list-style:none;margin-top:8px;font-size:11.5px;line-height:15px}
.links li{position:relative;padding-left:10px;margin-bottom:8px}
.links li::before{content:"·";position:absolute;left:0;color:#888}
.addr{margin-top:9px;font-size:11.5px;line-height:16px}
.addr .row{position:relative;padding-left:32px;margin-bottom:26px}
.addr svg{position:absolute;left:0;top:2px}
.map{position:absolute;left:635px;top:72px;width:236px;height:154px;background:linear-gradient(135deg,#e6e2da,#d2d7dc)}
.social{margin-top:14px}
.social .item{position:relative;height:38px;margin-bottom:24px;padding-left:49px}
.social .dot{position:absolute;left:0;top:0;width:32px;height:32px;border-radius:50%;background:var(--plum)}
.social b{display:block;font-size:12.5px;font-weight:400;color:var(--white);padding-top:5px}
.social small{display:block;font-size:8.5px;color:#666;margin-top:8px}
.copyright{position:absolute;left:0;top:2291px;width:1200px;height:41px;background:var(--plum);color:var(--white);font-size:12px;display:flex;align-items:center;justify-content:center}
</style>
</head>
<body>

<header class="site-header">
  <div class="topbar">
    <span class="contact mail">
      <svg width="14" height="11" viewBox="0 0 14 11"><rect width="14" height="11" fill="#fff"/><path d="M0 0l7 6 7-6" fill="none" stroke="#6b1d4d" stroke-width="1.4"/></svg>
      info@pixelbrook.co.uk
    </span>
    <span class="contact phone">
      <svg width="20" height="20" viewBox="0 0 20 20"><circle cx="10" cy="10" r="9" fill="none" stroke="#fff" stroke-width="1.5"/><path d="M7 5l2 2-1 2 3 3 2-1 2 2-2 2c-4 0-8-4-8-8z" fill="#fff"/></svg>
      01632 960418
    </span>
  </div>
  <div class="brand"><span class="brand-dot"></span><span class="brand-name">PixelBrook</span></div>
  <nav class="main-nav">
    <a class="nav-link nav-home">HOME</a>
    <a class="nav-link nav-about">ABOUT US</a>
    <a class="nav-link nav-services">OUR SERVICES</a>
    <a class="nav-link nav-contact">CONTACT US</a>
  </nav>
</header>

<section class="hero" role="img" aria-label="Slider photo: a hand holding a tablet with glowing app icons flying out, on a dark background">
  <div class="slide-arrow prev"><svg width="10" height="12"><path d="M8 1L2 6l6 5" fill="none" stroke="#fff" stroke-width="2"/></svg></div>
  <div class="slide-arrow next"><svg width="10" height="12"><path d="M2 1l6 5-6 5" fill="none" stroke="#fff" stroke-width="2"/></svg></div>
  <p class="hero-copy">We Work With Clients To Understand Their<br>Business &amp; Maximise Its Online Presence And<br>Goal To Reach The Destination</p>
  <div class="btn-start">Get Started</div>
</section>

<section class="welcome">
  <h2 class="sec-title">Welcome to PixelBrook</h2>
  <div class="divider"></div>
  <p class="welcome-text">Lorem ipsum dolor sit amet, consectetuer adipiscing elit, sed diam nonummy nibh euismod tincidunt ut laoreet dolore magna aliquam erat volutpat. Ut wisi enim ad minim veniam, lobortis nisl ut aliquip ex ea commodo consequat. Duis autem vel eum iriure dolor in hendrerit in vulputate velit esse molestie eros et dignissim qui blandit praesent luptatum zzril delenit augue duis dolore te feugait nulla facilisi.</p>
  <div class="btn-more">READ MORE</div>
</section>

<section class="services">
  <h2 class="sec-title">Our Services</h2>
  <div class="divider"></div>

  <svg class="abs" style="left:0;top:0" width="1200" height="772" viewBox="0 0 1200 772">
    <defs>
      <filter id="shadow" x="-30%" y="-30%" width="160%" height="160%"><feDropShadow dx="0" dy="4" stdDeviation="5" flood-opacity=".3"/></filter>
    </defs>
    <circle cx="600" cy="411" r="163" fill="#dfe5e8"/>
    <circle cx="600" cy="411" r="46" fill="none" stroke="#c9cfd4" stroke-width="6"/>
    <g stroke="#999" stroke-width="1.2" stroke-dasharray="2 2">
      <line x1="393" y1="242" x2="416" y2="286"/>
      <line x1="676" y1="158" x2="653" y2="202"/>
      <line x1="819" y1="365" x2="862" y2="388"/>
      <line x1="819" y1="543" x2="862" y2="567"/>
      <line x1="549" y1="649" x2="528" y2="691"/>
      <line x1="362" y1="427" x2="385" y2="470"/>
    </g>
    <g fill="#777">
      <circle cx="416" cy="286" r="2.5"/><circle cx="676" cy="158" r="2.5"/><circle cx="819" cy="365" r="2.5"/>
      <circle cx="819" cy="543" r="2.5"/><circle cx="549" cy="649" r="2.5"/><circle cx="362" cy="427" r="2.5"/>
    </g>
    <g filter="url(#shadow)" stroke="#fff" stroke-width="7">
      <circle cx="600" cy="256" r="52" fill="var(--circle)"/>
      <circle cx="737" cy="345" r="52" fill="var(--circle)"/>
      <circle cx="737" cy="505" r="52" fill="var(--circle)"/>
      <circle cx="600" cy="582" r="52" fill="var(--circle)"/>
      <circle cx="449" cy="505" r="52" fill="var(--circle)"/>
      <circle cx="449" cy="345" r="52" fill="var(--circle-seo)"/>
    </g>
    <g transform="translate(600 256)" fill="none" stroke="#fff" stroke-width="3">
      <circle r="16"/><circle r="7"/>
      <g stroke-width="5"><line y1="-17" y2="-24"/><line y1="17" y2="24"/><line x1="-17" x2="-24"/><line x1="17" x2="24"/>
      <line x1="12" y1="12" x2="17" y2="17"/><line x1="-12" y1="-12" x2="-17" y2="-17"/><line x1="12" y1="-12" x2="17" y2="-17"/><line x1="-12" y1="12" x2="-17" y2="17"/></g>
    </g>
    <g transform="translate(737 345)" fill="none" stroke="#fff" stroke-width="2.5">
      <rect x="-22" y="-12" width="44" height="28"/><path d="M-22 -12L0 6 22 -12M-22 16L-6 2M22 16L6 2"/>
    </g>
    <g transform="translate(737 505)" fill="#fff">
      <circle cx="-8" cy="-12" r="9"/><path d="M-26 20c0-14 8-20 18-20s14 4 16 8v12z"/>
      <rect x="2" y="2" width="24" height="16" fill="var(--circle)" stroke="#fff" stroke-width="2"/><path d="M2 2l12 9 12-9" fill="none" stroke="#fff" stroke-width="2"/>
    </g>
    <g transform="translate(600 582)" fill="none" stroke="#fff" stroke-width="2.5">
      <rect x="-16" y="-24" width="22" height="44" rx="3"/><line x1="-10" y1="14" x2="0" y2="14"/>
      <path d="M8 -8l14 -8v24l-14 -8z" fill="#fff"/>
    </g>
    <g transform="translate(449 505)" fill="none" stroke="#fff" stroke-width="2.5">
      <path d="M-20 4a10 10 0 0 1 2 -20a14 14 0 0 1 26 -2a10 10 0 0 1 12 22z"/>
      <rect x="-10" y="-8" width="20" height="6"/><rect x="-10" y="0" width="20" height="6"/>
      <line x1="0" y1="6" x2="0" y2="20"/><line x1="-12" y1="20" x2="12" y2="20"/>
    </g>
    <g transform="translate(449 345)" fill="none" stroke="#fff" stroke-width="3">
      <circle cx="10" cy="-3" r="11"/><line x1="18" y1="5" x2="28" y2="16" stroke-width="5"/>
      <text x="-29" y="3" fill="#fff" stroke="none" font-family="Lato, sans-serif" font-weight="700" font-size="15">SEO</text>
    </g>
  </svg>

  <div class="service seo right" style="left:97px;top:170px"><h3>Website Health Check (SEO)</h3><p>Sed ut perspiciatis unde omnis<br>sit voluptatem accusantium</p></div>
  <div class="service" style="left:688px;top:147px"><h3>Website Updating &amp; Development</h3><p>Sed ut perspiciatis unde omnis<br>sit voluptatem accusantium</p></div>
  <div class="service right" style="left:73px;top:358px"><h3>Website Hosting &amp; Management</h3><p>Sed ut perspiciatis unde omnis<br>sit voluptatem accusantium</p></div>
  <div class="service" style="left:875px;top:380px"><h3>Newsletter Management</h3><p>Sed ut perspiciatis unde omnis<br>sit voluptatem accusantium</p></div>
  <div class="service" style="left:867px;top:568px"><h3>Email Management</h3><p>Sed ut perspiciatis unde omnis<br>sit voluptatem accusantium</p></div>
  <div class="service right" style="left:207px;top:674px"><h3>Digital Marketing</h3><p>Sed ut perspiciatis unde omnis<br>sit voluptatem accusantium</p></div>
</section>

<section class="testimonials">
  <h2 class="sec-title">Client Testimonials</h2>
  <div class="divider"></div>
  <svg class="t-arrow" style="left:101px" width="16" height="26"><path d="M14 2L3 13l11 11" fill="none" stroke="var(--plum)" stroke-width="4"/></svg>
  <svg class="t-arrow" style="left:1076px" width="16" height="26"><path d="M2 2l11 11L2 24" fill="none" stroke="var(--plum)" stroke-width="4"/></svg>

  <figure class="quote" style="left:122px">
    <div class="headshot" role="img" aria-label="Headshot of a smiling client"></div>
    <span class="mark">“</span>
    <p>Lorem ipsum dolor sit amet,<br>consecer adscing elit, sed diam nonummy<br>Lorem ipsum dolor sit amet, consectetuer<br>adipiscing elit,</p>
    <cite>- Consectetue Radipiscing</cite>
  </figure>
  <figure class="quote" style="left:456px">
    <div class="headshot" role="img" aria-label="Headshot of a client in a shirt"></div>
    <span class="mark">“</span>
    <p>Lorem ipsum dolor sit amet,<br>consectetuer adipiscing elit, sed diam<br>nonummy  Lorem ipsum dolor sit amet,<br>consectetuer adipiscing elit,</p>
    <cite>- Diam Nonummy</cite>
  </figure>
  <figure class="quote" style="left:773px">
    <div class="headshot" role="img" aria-label="Headshot of a senior client in a suit"></div>
    <span class="mark">“</span>
    <p>Lorem ipsum dolor sit amet,<br>consectetuer adipiscing elit, sed diam<br>nonummy  Lorem ipsum dolor sit amet,<br>consectetuer adipiscing elit,</p>
    <cite>- Dolor Sitamet</cite>
  </figure>
</section>

<footer class="site-footer">
  <div class="f-col" style="left:131px">
    <h4>Quick <span>Links</span></h4>
    <ul class="links">
      <li>Digital Marketing About</li>
      <li>Zorvani Promoline Contact</li>
      <li>Chatterloop Advertising<br>Privacy Policy</li>
      <li>Search Engine Optimisation (SEO)<br>Terms &amp; Conditions</li>
      <li>Website Hosting FAQ</li>
      <li>Newsletter Management</li>
    </ul>
  </div>
  <div class="f-col" style="left:385px">
    <h4>Contact <span>Details</span></h4>
    <div class="addr">
      <div class="row"><svg width="12" height="16" viewBox="0 0 12 16"><path d="M6 0a6 6 0 0 1 6 6c0 4-6 10-6 10S0 10 0 6a6 6 0 0 1 6-6z" fill="var(--plum)"/><circle cx="6" cy="6" r="2" fill="#0d0d0d"/></svg>PixelBrook<br>14 Farrow Close<br>Dunmere Westshire<br>ZX47 3LT</div>
      <div class="row"><svg width="12" height="12" viewBox="0 0 12 12"><path d="M1 1l3 0 1 3-2 1a7 7 0 0 0 4 4l1-2 3 1v3c-6 0-10-4-10-10z" fill="var(--plum)"/></svg>01632 960418</div>
      <div class="row"><svg width="13" height="9" viewBox="0 0 13 9"><rect width="13" height="9" fill="var(--plum)"/><path d="M0 0l6.5 5L13 0" fill="none" stroke="#0d0d0d"/></svg>info@pixelbrook.co.uk</div>
    </div>
  </div>
  <div class="f-col" style="left:631px">
    <h4 style="width:240px">Location <span>Map</span></h4>
  </div>
  <div class="map" role="img" aria-label="Street map showing the office location with a red pin"></div>
  <div class="f-col" style="left:929px">
    <h4 style="width:136px">Follow <span>Us</span></h4>
    <div class="social">
      <div class="item"><span class="dot"></span><b>CHATTERLOOP</b><small>BECOME A FAN</small></div>
      <div class="item"><span class="dot"></span><b>GUILDNET</b><small>FOLLOW US</small></div>
      <div class="item"><span class="dot"></span><b>QUILLO</b><small>JOIN US ON</small></div>
    </div>
  </div>
</footer>
<div class="copyright">© 2016 Pixelbrook.All Rights Reserved.</div>

</body>
</html>
```